Young Accounting firm needing a captivating business card

We need a business card design that forces the person to look at the card because its either gold foil, plastic, or lettering pop up etc. We already have a logo with a specific gold color and we need to make it pop. We are an accounting firm. I need the words" accounting, payroll, licenses, audits, taxes" somewhere on the business card so as to describe what we do- preferably on the side where the logo is at.

Industry/Entity Type

Accounting

Contact Information for Business Card

Address 48276 9th Ave S Ste 305, Federal Way, WA 98117
Business Phone (360)418-2096
Fax (360)418-2157
Office Cell Phone (360)586-7319

Font styles to use
Serif

Colors
85abd2

Requirements
Must have
• It should state
• "Accounting" "Taxes" "Audits" "Licenses" "Payroll"
Nice to have
• Matte with gold foil, different textures, With Either a textured ivory background or gray blue slate background
Should not have
• colorful colors

```html
<!DOCTYPE html>
<html lang="en">
<head>
<meta charset="utf-8">
<title>Larkmont Ledger – Business Card</title>
<link rel="stylesheet" href="https://fonts.googleapis.com/css2?family=Lora:wght@400;600;700&display=swap">
<style>
  :root {
    --gold: #bb9e22;
    --gold-light: #d9c257;
    --gold-deep: #9c8318;
    --ink: #3a3a3a;
    --card: #ffffff;
    --backdrop: #ece8e0;
    --edge: #d8d4cc;
  }
  * { box-sizing: border-box; margin: 0; padding: 0; }
  html, body { width: 1200px; height: 1024px; overflow: hidden; }
  body {
    background: var(--backdrop);
    font-family: "Lora", Georgia, serif;
    display: flex;
    flex-direction: column;
    align-items: center;
    justify-content: center;
    gap: 64px;
  }
  .card {
    width: 700px;
    height: 400px;
    background: var(--card);
    box-shadow: 0 2px 0 var(--edge), 0 14px 30px rgba(0,0,0,.12);
    position: relative;
    overflow: hidden;
  }

  /* Front */
  .card-front { display: flex; align-items: center; padding: 0 50px 0 60px; }
  .brand-block { flex: 0 0 290px; display: flex; flex-direction: column; align-items: flex-start; gap: 24px; }
  .brand-square { width: 72px; height: 72px; background: var(--gold); }
  .brand-name { color: var(--gold); font-size: 32px; font-weight: 400; line-height: 1; white-space: nowrap; }
  .details { flex: 1; padding-left: 20px; }
  .person-name { color: var(--gold); font-size: 26px; font-weight: 700; letter-spacing: 0.5px; line-height: 1.1; white-space: nowrap; }
  .person-title { color: var(--ink); font-size: 17px; font-weight: 700; margin: 4px 0 16px; }
  .contact-list { list-style: none; }
  .contact-item { display: flex; align-items: flex-start; gap: 10px; color: var(--ink); font-size: 13.5px; line-height: 1.4; margin-bottom: 5px; white-space: nowrap; }
  .contact-item svg { flex: 0 0 14px; width: 14px; height: 14px; margin-top: 3px; fill: var(--gold); }
  .contact-label { color: var(--gold); font-weight: 600; }

  /* Back */
  .back-square {
    position: absolute;
    top: -40px; left: 70px;
    width: 280px; height: 280px;
    background: linear-gradient(135deg, var(--gold-deep) 0%, var(--gold-light) 45%, var(--gold) 60%, var(--gold-deep) 100%);
  }
  .back-name {
    position: absolute;
    right: 50px; bottom: 78px;
    color: var(--gold);
    font-size: 44px;
    font-weight: 400;
    line-height: 1;
    white-space: nowrap;
  }
  .services {
    position: absolute;
    right: 50px; bottom: 40px;
    color: var(--ink);
    font-size: 14px;
    letter-spacing: 1.5px;
    text-transform: uppercase;
    white-space: nowrap;
  }
  .services .sep { color: var(--gold); padding: 0 6px; }
</style>
</head>
<body>

  <section class="card card-front">
    <div class="brand-block">
      <div class="brand-square"></div>
      <div class="brand-name">Larkmont Ledger</div>
    </div>
    <div class="details">
      <h1 class="person-name">MARCUS HALE</h1>
      <p class="person-title">Director</p>
      <ul class="contact-list">
        <li class="contact-item">
          <svg viewBox="0 0 16 16"><path d="M8 0a5.5 5.5 0 0 0-5.5 5.5C2.5 10 8 16 8 16s5.5-6 5.5-10.5A5.5 5.5 0 0 0 8 0zm0 8a2.5 2.5 0 1 1 0-5 2.5 2.5 0 0 1 0 5z"/></svg>
          <span>48276 9th Ave S Ste 305,<br>Federal Way, WA 98117</span>
        </li>
        <li class="contact-item">
          <svg viewBox="0 0 16 16"><path d="M3.6 1l2.3 3.2-1.4 1.6a9 9 0 0 0 5.7 5.7l1.6-1.4L15 12.4 13.6 15C7 15 1 9 1 2.4z"/></svg>
          <span><span class="contact-label">T</span> (360)418-2096</span>
        </li>
        <li class="contact-item">
          <svg viewBox="0 0 16 16"><path d="M4 1h8v4H4zM1 6h14v6h-2v3H3v-3H1zM5 10v3h6v-3z"/></svg>
          <span><span class="contact-label">F</span> (360)418-2157</span>
        </li>
        <li class="contact-item">
          <svg viewBox="0 0 16 16"><path d="M4 0h8v16H4zM5.5 2v10h5V2z"/></svg>
          <span><span class="contact-label">C</span> (360)586-7319</span>
        </li>
        <li class="contact-item">
          <svg viewBox="0 0 16 16"><path d="M1 3h14v10H1zM1.8 3.8L8 9l6.2-5.2" stroke="#fff" stroke-width="1.2"/></svg>
          <span>info@LarkmontLedger.com</span>
        </li>
        <li class="contact-item">
          <svg viewBox="0 0 16 16"><circle cx="8" cy="8" r="7"/><path d="M1 8h14M8 1c2.5 2 2.5 12 0 14M8 1c-2.5 2-2.5 12 0 14" stroke="#fff" stroke-width="1" fill="none"/></svg>
          <span>www.LarkmontLedger.com</span>
        </li>
      </ul>
    </div>
  </section>

  <section class="card card-back">
    <div class="back-square"></div>
    <div class="back-name">Larkmont Ledger</div>
    <p class="services">Accounting<span class="sep">·</span>Taxes<span class="sep">·</span>Audits<span class="sep">·</span>Licenses<span class="sep">·</span>Payroll</p>
  </section>

</body>
</html>
```